Business card design needed for Marbury Medical Practice

We need a new design for our growing medical practice. Our previous design used blue, white and black. I would like to have a design with a baby, child, adult and grandparent on it. We look after a wide range of patients from newborns to 100 year olds.

Industry/Entity Type

Medical

Contact Information for Business Card

Marbury Medical Practice
14 Dunmore Rd Kellridge, NSW 2791
Ph 4820 3647 Fax 4913 2506
Dr Helen Voss Dr Andrea Pollard
Dr Wendy Trelawny Dr Janice Whitworth
Dr Tom Ashbrook Dr Neil Dunn-Foster
Open Mon- Fri 9-1, 2-5pm
Sat 9-12pm by appointment
web:www.marburymedix.com.au
email:marburymedix@mailzonex.com

```html
<!DOCTYPE html>
<html lang="en">
<head>
<meta charset="utf-8">
<title>Marbury Medical Practice – Business Card</title>
<link rel="stylesheet" href="https://fonts.googleapis.com/css2?family=Questrial&family=Arimo:wght@400;700&display=swap">
<style>
  :root {
    --page: #e9ebee;
    --card: #ffffff;
    --brand-blue: #1f78c1;
    --brand-green: #1f9a48;
    --ink: #1a1a1a;
    --stone-light: #eeeeee;
    --stone-mid: #c9c9c9;
    --stone-dark: #a9a9a9;
    --figure-blue: #3a8fd6;
  }
  * { box-sizing: border-box; margin: 0; padding: 0; }
  html, body { width: 1200px; height: 900px; overflow: hidden; }
  body {
    background: var(--page);
    font-family: "Arimo", Arial, sans-serif;
    color: var(--ink);
    position: relative;
  }
  .card {
    position: absolute;
    left: 290px;
    width: 620px;
    height: 354px;
    background: var(--card);
    overflow: hidden;
    box-shadow: 0 6px 18px rgba(0,0,0,0.18);
  }
  .card--front { top: 80px; }
  .card--back { top: 466px; }

  /* Wordmark: one colour, one weight */
  .wordmark {
    position: absolute;
    font-family: "Questrial", sans-serif;
    font-weight: 400;
    color: var(--brand-green);
    white-space: nowrap;
  }
  .wordmark__main { display: block; text-transform: uppercase; letter-spacing: 0.5px; }
  .wordmark__sub { display: block; }

  /* Front */
  .front-backdrop {
    position: absolute; inset: 0;
    background: radial-gradient(ellipse at 45% 45%, var(--stone-light) 0%, var(--stone-mid) 60%, var(--stone-dark) 100%);
  }
  .front-corner { position: absolute; inset: 0; }
  .front-figures {
    position: absolute;
    left: 170px; top: 24px;
    width: 270px; height: 116px;
    background: linear-gradient(90deg, rgba(58,143,214,0.55), rgba(58,143,214,0.85));
    border-radius: 4px;
  }
  .wordmark--front { left: 165px; top: 148px; }
  .wordmark--front .wordmark__main { font-size: 58px; line-height: 60px; }
  .wordmark--front .wordmark__sub { font-size: 28px; line-height: 32px; margin-left: 6px; }

  /* Back */
  .wordmark--back { left: 36px; top: 22px; }
  .wordmark--back .wordmark__main { font-size: 50px; line-height: 52px; }
  .wordmark--back .wordmark__sub { font-size: 25px; line-height: 30px; }
  .back-figures {
    position: absolute;
    right: 30px; top: 54px;
    width: 240px; height: 96px;
    background: linear-gradient(90deg, rgba(58,143,214,0.6), rgba(58,143,214,0.9));
    border-radius: 4px;
  }
  .contact-list {
    position: absolute;
    left: 36px; top: 158px;
    list-style: none;
    font-size: 14px;
    line-height: 20px;
  }
  .contact-list .label {
    display: inline-block;
    width: 24px;
    color: var(--brand-blue);
    font-weight: 700;
  }
  .doctor-list {
    position: absolute;
    left: 360px; top: 172px;
    list-style: none;
    font-size: 15px;
    line-height: 20px;
  }
  .doctor-list .title { font-weight: 700; }
  .hours-band {
    position: absolute;
    left: 0; right: 0; bottom: 0;
    height: 40px;
    background: var(--brand-blue);
    color: var(--ink);
    font-size: 15px;
    line-height: 40px;
    text-align: center;
  }
</style>
</head>
<body>

  <section class="card card--front" aria-label="Card front">
    <div class="front-backdrop" role="img" aria-label="Soft grey photograph of sandstone cliffs"></div>
    <svg class="front-corner" viewBox="0 0 620 354" aria-hidden="true">
      <path d="M620 120 C560 230 480 300 360 354 L620 354 Z" fill="var(--brand-blue)"/>
    </svg>
    <div class="front-figures" role="img" aria-label="Silhouettes of a child, adults and an elderly person walking in a line"></div>
    <div class="wordmark wordmark--front">
      <span class="wordmark__main">Marbury</span>
      <span class="wordmark__sub">Medical Practice</span>
    </div>
  </section>

  <section class="card card--back" aria-label="Card back">
    <div class="wordmark wordmark--back">
      <span class="wordmark__main">Marbury</span>
      <span class="wordmark__sub">Medical Practice</span>
    </div>
    <div class="back-figures" role="img" aria-label="Silhouettes of a child, adults and an elderly person walking in a line"></div>

    <ul class="contact-list">
      <li><span class="label">P:</span> 4820 3647</li>
      <li><span class="label">F:</span> 4913 2506</li>
      <li><span class="label">E:</span> marburymedix@mailzonex.com</li>
      <li><span class="label">A:</span> 14 Dunmore Rd Kellridge, NSW 2791</li>
      <li><span class="label">W:</span> www.marburymedix.com.au</li>
    </ul>

    <ul class="doctor-list">
      <li><span class="title">Dr.</span> Helen Voss</li>
      <li><span class="title">Dr.</span> Andrea Pollard</li>
      <li><span class="title">Dr.</span> Wendy Trelawny</li>
      <li><span class="title">Dr.</span> Janice Whitworth</li>
      <li><span class="title">Dr.</span> Tom Ashbrook</li>
      <li><span class="title">Dr.</span> Neil Dunn-Foster</li>
    </ul>

    <div class="hours-band">Open Mon- Fri 9-1, 2-5pm Sat 9-12pm by appointment</div>
  </section>

</body>
</html>
```